Here's your chance to make lots of children happy! Colourful and fun bag design for candies

Happy New Year 2019 to all you creative souls out there! It's time to create a design that would bring happiness to a lot of children, big and small, all around the world! We are updating our packaging to make it more colourful, attractive/cute and fun. This assignment is for a series of 5 designs for 5 different candy flavours - Coconut HARD Candy (with Western Australian Sea Salt), Coconut CHEWY candy, Cola, Mint, and Tamarind. The general look of the 5 packaging must be similar. To differentiate, please use different colours, product name (the above 5 flavours) and pictures representing the flavours. As you can see, from our old packaging, the designs are very fragmented. The front dimension of the bag is 145mm wide and 205mm height, including sealing area: Top seal - 25mm, bottom seal 15mm. Our parent logo is SunKite and appears on the top left. You may or may not include an open window to show the wrapped candies inside, depending on your design. Please see attached files for our old designs. You may use the included draft template as a guide, you may choose to use our old pictures or new ones. A couple of our latest packaging series are also attached. Other products can be found on our website - www.velortaq.com.my. Please do not use large areas of white or black as much as possible in your design.

Target Market(s)

Target audience - children for mint and cola, adults for coconut and tamarind

Font styles to use
Sans Serif

Requirements
Should not have
• Large blocks of white or black

```html
<!DOCTYPE html>
<html lang="en">
<head>
<meta charset="utf-8">
<title>SunKite Candy Bags</title>
<link href="https://fonts.googleapis.com/css2?family=Chewy&family=Luckiest+Guy&display=swap" rel="stylesheet">
<style>
  :root{
    --stage:#e4efee;
    --white:#ffffff;
    --ink:#1b1b24;
    --seal:#9ec9d9;
    --coco-top-a:#f7b843;
    --coco-top-b:#f8d53a;
    --coco-blob:#f5e23a;
    --coco-pink:#ee9cc4;
    --coco-pink-b:#f3c0dc;
    --sky:#8ccfe9;
    --sky-b:#5fc0e6;
    --mint-top-a:#b7d67a;
    --mint-top-b:#14aec8;
    --mint-wave:#1f9fdc;
    --mint-green:#a4c93a;
    --mint-green-b:#5fb04a;
    --candy:#f2eab8;
    --coconut-a:#8a6040;
    --coconut-b:#e9e2d6;
    --leaf-a:#4f9a3a;
    --leaf-b:#7cc05a;
  }
  *{margin:0;padding:0;box-sizing:border-box}
  html,body{width:1200px;height:697px;overflow:hidden;background:var(--stage)}
  .stage{position:relative;width:1200px;height:697px}
  .bag{position:absolute;top:83px;width:366px;height:521px;box-shadow:0 6px 14px rgba(0,0,0,.22)}
  .bag--coconut{left:118px}
  .bag--mint{left:721px}
  .bag svg{display:block;width:366px;height:521px}
  .brand-name{font-family:"Chewy",system-ui,sans-serif;font-size:13px;fill:var(--ink)}
  .tagline{font-family:"Chewy",system-ui,sans-serif;font-size:14px;fill:var(--white);stroke:var(--ink);stroke-width:3px;paint-order:stroke}
  .flavour-title{font-family:"Luckiest Guy",system-ui,sans-serif;font-size:58px;fill:var(--white);stroke:var(--ink);stroke-width:7px;paint-order:stroke;letter-spacing:-1px}
  .flavour-sub{font-family:"Luckiest Guy",system-ui,sans-serif;font-size:30px;fill:var(--white);stroke:var(--ink);stroke-width:5px;paint-order:stroke}
  .net-weight{font-family:Arial,Helvetica,sans-serif;font-size:7px;fill:var(--ink)}
  .seal-line{stroke:var(--seal);stroke-width:1}
</style>
</head>
<body>
<main class="stage">

  <!-- Coconut bag -->
  <section class="bag bag--coconut">
    <svg viewBox="0 0 366 521" xmlns="http://www.w3.org/2000/svg">
      <defs>
        <linearGradient id="cocoTop" x1="0" y1="0" x2="0" y2="1">
          <stop offset="0" stop-color="var(--coco-top-a)"/>
          <stop offset="1" stop-color="var(--coco-top-b)"/>
        </linearGradient>
        <linearGradient id="cocoPink" x1="0" y1="0" x2="1" y2="0">
          <stop offset="0" stop-color="var(--coco-pink-b)"/>
          <stop offset="1" stop-color="var(--coco-pink)"/>
        </linearGradient>
        <linearGradient id="skyBottom" x1="0" y1="0" x2="0" y2="1">
          <stop offset="0" stop-color="var(--sky)"/>
          <stop offset="1" stop-color="var(--sky-b)"/>
        </linearGradient>
        <linearGradient id="coconutFill" x1="0" y1="0" x2="0" y2="1">
          <stop offset="0" stop-color="var(--coconut-a)"/>
          <stop offset=".6" stop-color="var(--coconut-a)"/>
          <stop offset=".75" stop-color="var(--coconut-b)"/>
          <stop offset="1" stop-color="var(--coconut-b)"/>
        </linearGradient>
      </defs>
      <rect class="bag-base" width="366" height="521" fill="var(--white)"/>
      <path class="top-wave" fill="url(#cocoTop)" d="M0 0H366V120C330 118 300 150 280 160C240 150 200 140 160 148C110 158 60 140 0 150Z"/>
      <path class="side-blob" fill="var(--coco-blob)" d="M366 105C330 100 318 135 328 175C338 220 305 260 320 300C330 325 350 335 366 338Z"/>
      <path class="pink-wave" fill="url(#cocoPink)" d="M0 330C40 305 95 300 135 322C175 345 210 350 245 335C285 318 320 330 345 345L366 352V521H0Z"/>
      <path class="sky-wave" fill="url(#skyBottom)" d="M0 415C60 398 120 412 180 408C240 404 285 380 330 392C348 397 366 404 366 404V521H0Z"/>
      <path role="img" aria-label="Photo of a whole coconut above an opened coconut half" fill="url(#coconutFill)" d="M104 140C150 125 210 135 285 140C290 200 280 250 250 290C285 310 300 360 288 383H150C140 345 160 310 200 292C150 270 100 210 104 140Z"/>
      <g role="img" aria-label="Two wrapped cream candies">
        <ellipse cx="268" cy="430" rx="26" ry="15" fill="var(--candy)"/>
        <ellipse cx="300" cy="446" rx="26" ry="15" fill="var(--candy)"/>
      </g>
      <line class="seal-line" x1="0" y1="57" x2="366" y2="57"/>
      <line class="seal-line" x1="0" y1="482" x2="366" y2="482"/>
      <g class="brand">
        <rect x="22" y="73" width="86" height="24" fill="var(--white)" stroke="var(--ink)" stroke-width="1"/>
        <rect x="27" y="79" width="12" height="12" fill="#d6262a"/>
        <text class="brand-name" x="44" y="90">SunKite</text>
      </g>
      <text class="tagline" x="360" y="90" text-anchor="end">Cremocy, Roasted coconut Flavour</text>
      <text class="flavour-title" x="14" y="438">COCONUT</text>
      <text class="flavour-sub" x="30" y="472">CANDY</text>
      <text class="net-weight" transform="translate(358 470) rotate(-90)">Net Wt./ Berat Bersih: 200gm</text>
    </svg>
  </section>

  <!-- Mint bag -->
  <section class="bag bag--mint">
    <svg viewBox="0 0 366 521" xmlns="http://www.w3.org/2000/svg">
      <defs>
        <linearGradient id="mintTop" x1="0" y1="0" x2="0" y2="1">
          <stop offset="0" stop-color="var(--mint-top-a)"/>
          <stop offset=".6" stop-color="var(--mint-top-b)"/>
          <stop offset="1" stop-color="var(--mint-wave)"/>
        </linearGradient>
        <linearGradient id="mintGreen" x1="0" y1="0" x2="1" y2="0">
          <stop offset="0" stop-color="var(--mint-green)"/>
          <stop offset="1" stop-color="var(--mint-green-b)"/>
        </linearGradient>
        <linearGradient id="skyBottomMint" x1="0" y1="0" x2="0" y2="1">
          <stop offset="0" stop-color="var(--sky)"/>
          <stop offset="1" stop-color="var(--sky-b)"/>
        </linearGradient>
        <linearGradient id="leafFill" x1="0" y1="0" x2="1" y2="1">
          <stop offset="0" stop-color="var(--leaf-b)"/>
          <stop offset="1" stop-color="var(--leaf-a)"/>
        </linearGradient>
      </defs>
      <rect class="bag-base" width="366" height="521" fill="var(--white)"/>
      <path class="top-wave" fill="url(#mintTop)" d="M0 0H366V120C330 118 300 150 280 160C240 150 200 140 160 148C110 158 60 140 0 150Z"/>
      <path class="side-blob" fill="var(--mint-wave)" d="M366 105C330 100 318 135 328 175C338 220 305 260 320 300C330 325 350 335 366 338Z"/>
      <path class="green-wave" fill="url(#mintGreen)" d="M0 330C40 305 95 300 135 322C175 345 210 350 245 335C285 318 320 330 345 345L366 352V521H0Z"/>
      <path class="sky-wave" fill="url(#skyBottomMint)" d="M0 415C60 398 120 412 180 408C240 404 285 380 330 392C348 397 366 404 366 404V521H0Z"/>
      <path role="img" aria-label="Photo of fresh mint leaves in two sprigs" fill="url(#leafFill)" d="M115 135C160 125 230 140 275 150C285 200 270 240 250 255C275 290 265 360 240 380H160C130 340 130 300 150 275C120 250 105 190 115 135Z"/>
      <g role="img" aria-label="Two wrapped mint candies">
        <ellipse cx="268" cy="430" rx="26" ry="15" fill="var(--candy)"/>
        <ellipse cx="300" cy="446" rx="26" ry="15" fill="var(--candy)"/>
      </g>
      <line class="seal-line" x1="0" y1="57" x2="366" y2="57"/>
      <line class="seal-line" x1="0" y1="482" x2="366" y2="482"/>
      <g class="brand">
        <rect x="20" y="73" width="86" height="24" fill="var(--white)" stroke="var(--ink)" stroke-width="1"/>
        <rect x="25" y="79" width="12" height="12" fill="#d6262a"/>
        <text class="brand-name" x="42" y="90">SunKite</text>
      </g>
      <text class="tagline" x="340" y="90" text-anchor="end">Refreshing, coll and shoofting</text>
      <text class="flavour-title" x="14" y="438">MINT</text>
      <text class="flavour-sub" x="30" y="472">CANDY</text>
      <text class="net-weight" transform="translate(358 470) rotate(-90)">Net Wt./ Berat Bersih: 200gm</text>
    </svg>
  </section>

</main>
</body>
</html>
```